Welding and farication business card

Business name Tmb Welding & Fabrication

I need a business card made for my welding and fabrication business that is bold and stands out. My business is both welding repairs on machinery and anything else you can imagine as well as fabricating new products. i have used this service before and was very happy with the out come of my design logo. i think the card should remain fairly simple and classy but also be bold. I think a black card would best be suited to the talk with my logo on it. i feel the back of the card should just have my logo and the front have my logo email, website and phone number and maybe incorporate a pagebook and snapgallery simple if it can be made look good these arnt a necessity.
I have included both my logo and some business card ideas below

Target Market(s)

Farmers, heavy industry, earthmoving, trucking

Industry/Entity Type

Engineering

Contact Information for Business Card

0438517264
dane@tmbweldingandfabrication.com.au
www.tmbweldingandfabrication.com.au

Colors
33a6d7
0255a3

Requirements
Must have
• Dane Whitlock
my phone number 0438517264
my logo
Preferably a black card desgn
Nice to have
• List of what i do,
Sheds and carports
Ute trays
Stockyards
Trailers
Farm equipment
Stockcrates
Gateways and Entrances
Breakdowns
Maintenance
And lots more!

```html
<!DOCTYPE html>
<html lang="en">
<head>
<meta charset="utf-8">
<title>Tmb Welding &amp; Fabrication — Business Card</title>
<link rel="stylesheet" href="https://fonts.googleapis.com/css2?family=Montserrat:wght@400;500;700;800;900&display=swap">
<style>
  :root {
    --card-black: #000000;
    --steel-grey: #4a5563;
    --brand-blue: #0255a3;
    --spark-blue: #33a6d7;
    --ink-white: #ffffff;
    --backdrop: #e9e9e7;
  }
  * { margin: 0; padding: 0; box-sizing: border-box; }
  html, body {
    width: 1200px; height: 800px; overflow: hidden;
    background: var(--backdrop);
    font-family: "Montserrat", Arial, sans-serif;
  }
  .canvas { position: relative; width: 1200px; height: 800px; }

  .card {
    position: absolute; left: 341px; width: 588px; height: 336px;
    background: var(--card-black); overflow: hidden; color: var(--ink-white);
    box-shadow: 0 3px 10px rgba(0,0,0,0.25);
  }
  .card--front { top: 35px; }
  .card--back { top: 420px; }

  /* Front */
  .brand-mark { position: absolute; left: 48px; top: 12px; color: var(--brand-blue); font-weight: 900; }
  .brand-mark__dot {
    position: absolute; left: 0; top: 18px; width: 22px; height: 22px;
    border-radius: 50%; background: var(--spark-blue);
  }
  .brand-mark__initials { display: block; margin-left: 34px; font-size: 108px; line-height: 1; letter-spacing: -2px; }
  .brand-mark__descriptor { display: block; margin-left: 36px; margin-top: 2px; font-size: 20px; line-height: 1; letter-spacing: 0.5px; }

  .phone {
    position: absolute; right: 95px; top: 170px;
    font-size: 46px; font-weight: 800; line-height: 1; letter-spacing: -0.5px; white-space: nowrap;
    transform: rotate(-10deg); transform-origin: right bottom;
  }
  .web-contact {
    position: absolute; right: 107px; top: 244px;
    font-size: 16.5px; font-weight: 500; line-height: 1.15; text-align: right; white-space: nowrap;
    transform: rotate(-5.5deg); transform-origin: right bottom;
  }

  .name-band { position: absolute; right: 0; top: 0; width: 89px; height: 100%; background: var(--steel-grey); }
  .name-band__name {
    position: absolute; left: 50%; top: 50%;
    transform: translate(-50%, -50%) rotate(-90deg);
    white-space: nowrap; font-size: 32px; font-weight: 800; letter-spacing: 0.5px; text-transform: uppercase;
  }

  /* Back */
  .services-heading {
    position: absolute; left: 48px; top: 6px;
    writing-mode: vertical-rl; font-size: 21px; font-weight: 800; line-height: 1;
  }
  .services-rule { position: absolute; left: 94px; top: 0; width: 5px; height: 180px; background: var(--steel-grey); }
  .services-list { position: absolute; left: 123px; top: 12px; list-style: none; font-size: 17px; font-weight: 500; line-height: 21px; }
  .services-list strong { font-weight: 800; }

  .more-block { position: absolute; left: 127px; top: 218px; width: 123px; height: 118px; background: var(--steel-grey); overflow: hidden; }
  .more-block__text {
    position: absolute; left: -4px; top: 2px; color: var(--card-black);
    font-size: 40px; font-weight: 900; line-height: 38px; letter-spacing: -1px;
  }

  .back-mark { position: absolute; left: 426px; top: 262px; display: flex; align-items: center; gap: 8px; color: var(--steel-grey); font-weight: 900; }
  .back-mark__dot { width: 10px; height: 10px; border-radius: 50%; background: var(--steel-grey); }
  .back-mark__initials { font-size: 44px; line-height: 1; letter-spacing: -1px; }
</style>
</head>
<body>
<main class="canvas">

  <section class="card card--front" aria-label="Card front">
    <div class="brand-mark">
      <span class="brand-mark__dot"></span>
      <span class="brand-mark__initials">TMB</span>
      <span class="brand-mark__descriptor">WELDING &amp; FABRICATION</span>
    </div>
    <p class="phone">0438517264</p>
    <p class="web-contact">
      www.tmbweldingandfabrication.com.au<br>
      dane@tmbweldingandfabrication.com.au
    </p>
    <div class="name-band"><span class="name-band__name">Dane Whitlock</span></div>
  </section>

  <section class="card card--back" aria-label="Card back">
    <h2 class="services-heading">MY Services</h2>
    <div class="services-rule"></div>
    <ul class="services-list">
      <li>Sheds and carports</li>
      <li>Ute trays</li>
      <li>Stock<strong>YARDS</strong></li>
      <li>Trailers</li>
      <li><strong>FARM EQUIPMENT</strong></li>
      <li>Stockcrates</li>
      <li><strong>Gateways</strong> and Entrances</li>
      <li><strong>BREAK</strong>downs</li>
      <li>Maintenance</li>
    </ul>
    <div class="more-block"><p class="more-block__text">AND<br>LOTS<br>MORE</p></div>
    <div class="back-mark">
      <span class="back-mark__dot"></span>
      <span class="back-mark__initials">TMB</span>
    </div>
  </section>

</main>
</body>
</html>
```